Web design required

1-We need a web design for existing company based in New Zealand
2-We build residential house and light commercial
3-We has in-house designer which allow us can provide interior design
4-We modeling project before site construction, which enable both client and construction team to visually analysis whole project,

Target Market(s)

middle class residential house market
Ref: http://www.brambleworthbuilders.co.nz/

Industry/Entity Type

Construction Company

Number of Pages Required

1 page

Font styles to use
Sans Serif
Other font styles liked:
• Such as : Central Gothic or similar which has more design taste

Colors

Designer to choose colors to be used in the design.

Requirements
Must have
• Front sheet, contact information, sample project

```html
<!DOCTYPE html>
<html lang="en">
<head>
<meta charset="utf-8">
<title>Kereru Homes</title>
<link href="https://fonts.googleapis.com/css2?family=Montserrat:wght@400;500;600&family=Play:wght@400;700&display=swap" rel="stylesheet">
<style>
:root{
  --black:#000;
  --white:#fff;
  --panel:rgba(20,14,12,.78);
  --panel-soft:rgba(60,60,60,.72);
  --grey-text:#d9d9d9;
  --muted:#8a8a8a;
  --amber:#d8926a;
  --photo-dark:#2b2a2d;
}
*{box-sizing:border-box;margin:0;padding:0}
html,body{width:1200px;height:2629px;overflow:hidden;background:var(--black)}
body{position:relative;font-family:"Play",sans-serif;color:var(--white)}
.abs{position:absolute}

/* header */
.site-header{left:0;top:0;width:1200px;height:92px;background:var(--black)}
.brand{left:28px;top:27px;display:flex;align-items:center;gap:14px;font-family:"Montserrat",sans-serif;font-weight:500;font-size:25px;letter-spacing:.5px}
.brand-dot{width:38px;height:38px;border:3px solid var(--white);border-radius:50%}
.main-nav{right:26px;top:30px;display:flex;font-family:"Play",sans-serif;font-size:18px}
.main-nav a{color:var(--white);text-decoration:none}
.main-nav a.current{color:var(--muted)}
.main-nav .sep{margin:0 18px}

/* hero */
.hero{left:0;top:92px;width:1200px;height:813px;background:linear-gradient(100deg,#5a2a1f 0%,#4b5a3a 22%,#6b5a2a 35%,#3d4250 50%,#6a1a18 70%,#8a1d1a 100%)}
.hero-mark{left:566px;top:270px;width:68px;height:68px;border:5px solid var(--white);border-radius:50%}
.hero-title{left:0;top:370px;width:1200px;text-align:center;font-family:"Montserrat",sans-serif;font-weight:500;font-size:44px;letter-spacing:.5px}
.services{left:79px;top:577px;width:1042px;height:328px;background:rgba(0,0,0,.55);border-radius:42px 42px 0 0}
.service-photo{top:612px;width:296px;height:209px;border-radius:28px}
.service-label{top:832px;width:296px;text-align:center;font-family:"Montserrat",sans-serif;font-weight:500;font-size:22px;line-height:27px}
.s1{left:115px}.s2{left:452px}.s3{left:788px}

.accent-band{left:0;top:905px;width:1200px;height:22px;background:linear-gradient(90deg,#b87a5c,#e0a27e 50%,#b87a5c)}

/* section bars */
.section-bar{left:0;width:1200px;background:var(--black)}
.section-bar h2{position:absolute;left:38px;font-family:"Montserrat",sans-serif;font-weight:500;font-size:33px}
.bar-about{top:927px;height:93px}.bar-about h2{top:24px}
.bar-portfolio{top:1385px;height:94px}.bar-portfolio h2{top:25px}
.bar-blog{top:1924px;height:97px}.bar-blog h2{top:27px}

/* about */
.about{left:0;top:1020px;width:1200px;height:365px;background:linear-gradient(180deg,#c68664 0%,#7a5a4c 40%,#8a7c78 100%)}
.about-panel{left:18px;top:1041px;width:1165px;height:322px;background:var(--panel)}
.about-photo{left:106px;top:1098px;width:215px;height:208px;background:linear-gradient(160deg,#9cc0e0,#3f6f8c 55%,#1d3a45)}
.about-text{left:362px;top:1124px;width:732px;font-size:15.3px;line-height:23px;text-align:justify;color:var(--white)}

/* portfolio */
.portfolio{left:0;top:1479px;width:1200px;height:445px;background:linear-gradient(180deg,#7c8796,#9aa0a6 60%,#6d7278)}
.work{top:1504px;height:402px;border:1px solid #666}
.w1{left:18px;width:379px;background:linear-gradient(160deg,#2c54a8 0%,#8a8f98 55%,#c85a2a 80%,#5c5c60)}
.w2{left:411px;width:378px;background:linear-gradient(170deg,#3a3a3c,#6b6d70 50%,#d0702a 85%)}
.w3{left:807px;width:376px;background:linear-gradient(180deg,#2e64c0 0%,#4a8fd8 30%,#c8a870 55%,#8d7c62 100%)}

/* blog */
.blog{left:0;top:2021px;width:1200px;height:358px;background:linear-gradient(90deg,#7d8794,#b9a27a 45%,#8a8f96)}
.post-photo{top:2047px;height:309px}
.p1{left:18px;width:291px;background:linear-gradient(180deg,#8e7fb5,#5a4a5a 55%,#2a1f22)}
.p2{left:602px;width:289px;background:linear-gradient(180deg,#6aa0e0,#b7c6d8 35%,#8a6a52 70%,#5a7a3a)}
.post-body{top:2047px;height:309px;background:var(--panel-soft);padding:18px 12px 0 12px}
.b1{left:312px;width:283px}.b2{left:898px;width:285px}
.post-title{font-family:"Play",sans-serif;font-weight:700;font-size:17px;color:#c9c9c9;margin-bottom:21px}
.post-excerpt{font-size:15.3px;line-height:23px;text-align:justify;color:var(--white)}
.read-more{top:2321px;width:115px;height:32px;background:var(--black);border:1px solid #777;font-size:16px;line-height:30px;text-align:center}
.r1{left:319px}.r2{left:905px}

/* footer */
.site-footer{left:0;top:2379px;width:1200px;height:250px;background:var(--black)}
.contact{left:71px;top:2415px;font-size:18.5px;line-height:27px}
.contact strong{font-family:"Montserrat",sans-serif;font-weight:500;font-size:21px}
.footer-mark{left:575px;top:2442px;width:50px;height:50px;border:4px solid var(--white);border-radius:50%}
.footer-name{left:0;top:2503px;width:1200px;text-align:center;font-family:"Montserrat",sans-serif;font-weight:500;font-size:26px}
.copyright{left:0;top:2539px;width:1200px;text-align:center;font-size:17px}
.social-head{left:880px;top:2494px;width:255px;text-align:center;font-size:18px}
.social{left:884px;top:2537px;display:flex;gap:6px}
.social span{width:33px;height:33px;border-radius:50%;background:var(--white)}
</style>
</head>
<body>
<header class="site-header abs">
  <div class="brand abs"><span class="brand-dot"></span>KERERU HOMES</div>
  <nav class="main-nav abs">
    <a class="current" href="#">Home</a><span class="sep">|</span>
    <a href="#">Services</a><span class="sep">|</span>
    <a href="#">About</a><span class="sep">|</span>
    <a href="#">Portfolio</a><span class="sep">|</span>
    <a href="#">Blog</a><span class="sep">|</span>
    <a href="#">Contact</a>
  </nav>
</header>

<section class="hero abs" role="img" aria-label="Colourful high-rise apartment facades seen from below"></section>
<div class="hero-mark abs"></div>
<h1 class="hero-title abs">WELCOME TO KERERU HOMES</h1>
<div class="services abs"></div>
<div class="service-photo s1 abs" role="img" aria-label="Hands drawing building plans" style="background:linear-gradient(160deg,#f2f2f2,#c9c9c9 60%,#7a7a7a)"></div>
<div class="service-photo s2 abs" role="img" aria-label="Two-storey suburban house" style="background:linear-gradient(180deg,#8fb0d8,#a0a3a8 45%,#4f7a35)"></div>
<div class="service-photo s3 abs" role="img" aria-label="Site team reviewing plans on the ground" style="background:linear-gradient(180deg,#8a8880,#6e6a62 55%,#c9c2b0)"></div>
<div class="service-label s1 abs">Preconstruction<br>Planning</div>
<div class="service-label s2 abs">Construction<br>Modelling</div>
<div class="service-label s3 abs">Full Project<br>Management</div>

<div class="accent-band abs"></div>

<div class="section-bar bar-about abs"><h2>About</h2></div>
<section class="about abs" role="img" aria-label="Construction site silhouettes at sunset"></section>
<div class="about-panel abs"></div>
<div class="about-photo abs" role="img" aria-label="Glass office tower with sunlight"></div>
<p class="about-text abs">Lorem ipsum dolor sit amet, consectetuer adipiscing elit, sed diam nonummy nibh euismod tincidunt ut laoreet dolore magna aliquam erat volutpat. Ut wisi enim ad minim veniam, quis nostrud exerci tation ullamcorper suscipit lobortis nisl ut aliquip ex ea commodo consequat. Duis autem vel eum iriure dolor in hendrerit in vulputate velit esse molestie consequat, vel illum dolore eu feugiat nulla facilisis at vero eros et accumsan et iusto odio dignissim qui blandit praesent luptatum zzril delenit augue duis dolore te feugait nulla facilisi.</p>

<div class="section-bar bar-portfolio abs"><h2>Portfolio</h2></div>
<section class="portfolio abs" role="img" aria-label="Blurred construction site backdrop"></section>
<div class="work w1 abs" role="img" aria-label="Worker on a steel frame against blue sky"></div>
<div class="work w2 abs" role="img" aria-label="Site supervisor in hi-vis beside a truck"></div>
<div class="work w3 abs" role="img" aria-label="Timber house frame under construction"></div>

<div class="section-bar bar-blog abs"><h2>Blog</h2></div>
<section class="blog abs" role="img" aria-label="Blurred builder in hi-vis backdrop"></section>
<div class="post-photo p1 abs" role="img" aria-label="Modern house lit at dusk"></div>
<article class="post-body b1 abs">
  <h3 class="post-title">Lorem ipsum dolor sit amet</h3>
  <p class="post-excerpt">Lorem ipsum dolor sit amet, consectetuer adipiscing elit, sed diam nonummy nibh euismod tincidunt ut laoreet dolore magna aliquam erat volutpat. Ut wisi enim ad minim veniam, quis nostrud exerci tation ullamcorper suscipit blandit praesent luptatum zzril delenit.</p>
</article>
<div class="read-more r1 abs">Read More</div>
<div class="post-photo p2 abs" role="img" aria-label="Stone-clad family home entrance"></div>
<article class="post-body b2 abs">
  <h3 class="post-title">Lorem ipsum dolor sit amet</h3>
  <p class="post-excerpt">Lorem ipsum dolor sit amet, consectetuer adipiscing elit, sed diam nonummy nibh euismod tincidunt ut laoreet dolore magna aliquam erat volutpat. Ut wisi enim ad minim veniam, quis nostrud exerci tation ullamcorper suscipit blandit praesent luptatum zzril delenit.</p>
</article>
<div class="read-more r2 abs">Read More</div>

<footer class="site-footer abs"></footer>
<address class="contact abs" style="font-style:normal">
  <strong>KERERU HOMES</strong><br>
  18 Harbourview Lane<br>
  Eastfield<br>
  Auckland<br>
  Tel: 09 555 0142<br>
  E-Mail: info@kererehomes.co.nz
</address>
<div class="footer-mark abs"></div>
<div class="footer-name abs">KERERU HOMES</div>
<div class="copyright abs">© Kereru Homes Construction 2017.</div>
<div class="social-head abs">Communicate with us:</div>
<div class="social abs"><span></span><span></span><span></span><span></span><span></span><span></span></div>
</body>
</html>
```